Bref créative
Valmirock Stationary Design
Business Cards, Letterhead, etc....
Professional
Dorian K. Pelletrow
Chief Executive Officer
2718 N. Birch Ln.
Suite K-42
Tempe, AZ 85107-3318
XXX-XXX-XXXX
dorian@valmirock-example.com
http://www.valmirock-example.com/
See our website for our business areas and marketing information.
Back of the business card should be branded, but simple. Maybe our company monogram. There should be enough space to write notes on the back of the card.
Contains several versions of our logo for stationary design.

```html
<!DOCTYPE html>
<html lang="en">
<head>
<meta charset="utf-8">
<title>Valmirock Business Card</title>
<link href="https://fonts.googleapis.com/css2?family=Arimo:wght@400;700&display=swap" rel="stylesheet">
<style>
  :root {
    --bg: #dcdfe2;
    --teal-dark: #0b3f55;
    --teal: #146c87;
    --teal-light: #3fa6bf;
    --card-white: #ffffff;
    --card-grey: #e9ecee;
    --ink: #2b3238;
    --ink-soft: #6a737a;
  }
  * { margin: 0; padding: 0; box-sizing: border-box; }
  html, body { width: 1200px; height: 926px; overflow: hidden; }
  body {
    background: var(--bg);
    font-family: "Arimo", Arial, sans-serif;
    display: flex;
    align-items: center;
    justify-content: center;
    gap: 60px;
  }
  .card {
    position: relative;
    width: 520px;
    height: 310px;
    border-radius: 22px;
    overflow: hidden;
    background: var(--card-white);
    box-shadow: 0 6px 18px rgba(0,0,0,.18);
  }
  .card-art { position: absolute; inset: 0; width: 100%; height: 100%; }

  /* front */
  .card-front { background: linear-gradient(180deg, var(--card-grey), var(--card-white) 60%); }
  .holder { position: absolute; top: 24px; right: 34px; text-align: right; }
  .holder-name { font-size: 17px; font-weight: 700; color: var(--ink); }
  .holder-title { font-size: 12px; color: var(--ink-soft); margin-top: 3px; }
  .contact {
    position: absolute; top: 85px; right: 34px; width: 186px;
    list-style: none; font-size: 11px; line-height: 15px; color: var(--ink);
  }
  .contact li { display: flex; align-items: center; gap: 7px; white-space: nowrap; }
  .contact .dot { width: 6px; height: 6px; border-radius: 50%; background: var(--teal); flex: none; }
  .contact .blank { width: 6px; flex: none; }
  .contact .light { color: #fff; }
  .contact .light .dot { background: #fff; }
  .contact .light-first { margin-top: 14px; }
  .brand {
    position: absolute; left: 38px; bottom: 40px;
    display: flex; align-items: center; gap: 12px;
  }
  .brand-mark { width: 34px; height: 34px; border-radius: 50%; background: #fff; }
  .brand-name { font-size: 28px; font-weight: 700; color: #fff; letter-spacing: 1px; text-transform: uppercase; }

  /* back */
  .notes-label { position: absolute; top: 16px; left: 22px; font-size: 13px; font-weight: 700; color: #fff; }
  .back-mark {
    position: absolute; right: 36px; bottom: 30px;
    width: 38px; height: 38px; border-radius: 50%; background: var(--teal);
  }
</style>
</head>
<body>

<section class="card card-front">
  <svg class="card-art" viewBox="0 0 520 310" preserveAspectRatio="none" aria-hidden="true">
    <defs>
      <linearGradient id="waveFill" x1="0" y1="0" x2="1" y2="0">
        <stop offset="0" stop-color="#0b3f55"/>
        <stop offset="0.55" stop-color="#146c87"/>
        <stop offset="1" stop-color="#3fa6bf"/>
      </linearGradient>
    </defs>
    <path d="M0 216 C100 176 180 216 260 181 C280 172 292 163 310 161 C380 161 460 159 520 157 L520 310 L0 310 Z" fill="#9fd0dc" opacity=".7"/>
    <path d="M0 225 C100 185 180 225 260 190 C280 181 292 172 310 170 C380 170 460 168 520 166 L520 310 L0 310 Z" fill="url(#waveFill)"/>
  </svg>

  <div class="holder">
    <p class="holder-name">Dorian K. Pelletrow</p>
    <p class="holder-title">Chief Executive Officer</p>
  </div>

  <ul class="contact">
    <li><span class="dot"></span>2718 N. Birch Ln.</li>
    <li><span class="blank"></span>Suite K-42</li>
    <li><span class="blank"></span>Tempe, AZ 85107-3318</li>
    <li><span class="dot"></span>XXX-XXX-XXXX</li>
    <li><span class="dot"></span>XXX-XXX-XXXX</li>
    <li class="light light-first"><span class="dot"></span>XXX-XXX-XXXX</li>
    <li class="light"><span class="dot"></span>dorian@valmirock-example.com</li>
    <li class="light"><span class="dot"></span>http://www.valmirock-example.com/</li>
  </ul>

  <div class="brand">
    <span class="brand-mark"></span>
    <span class="brand-name">Valmirock</span>
  </div>
</section>

<section class="card card-back">
  <svg class="card-art" viewBox="0 0 520 310" preserveAspectRatio="none" aria-hidden="true">
    <defs>
      <linearGradient id="swoosh" x1="0" y1="0" x2="1" y2="0">
        <stop offset="0" stop-color="#0b3f55"/>
        <stop offset="1" stop-color="#146c87"/>
      </linearGradient>
    </defs>
    <path d="M0 0 L520 0 L520 6 C400 6 300 16 210 34 C120 52 60 62 0 66 Z" fill="#9fd0dc" opacity=".6"/>
    <path d="M0 0 L520 0 C400 0 300 8 210 26 C120 44 60 52 0 56 Z" fill="url(#swoosh)"/>
  </svg>
  <p class="notes-label">Notes :</p>
  <span class="back-mark"></span>
</section>

</body>
</html>
```